Life Coaching Business - needs business card design with logo

I need a business card and logo design for a life coaching business I started based in Los Angeles. I offer services to clients that wish to bring more balance and overall wholeness to their lives. As of right now, the business name is "Marcus Ellery Coaching." An iidea I had for the logo was to be kind of a Yin-Yang symbol but with dolphins, as the dolphin has symbolic meaning for my business. Although I am really open to other ideas as long as it incorporates the idea of “balance,” “wholeness,” and “dolphins.”I also wanted to incorporate the color blue, maybe in the form of water, waves, or some sort of peaceful imagery.

```html
<!DOCTYPE html>
<html lang="en">
<head>
<meta charset="utf-8">
<title>Marcus Ellery Coaching — Business Card</title>
<link rel="stylesheet" href="https://fonts.googleapis.com/css2?family=Cinzel:wght@700&family=Questrial&display=swap">
<style>
  :root {
    --stage: #2a2a2c;
    --card: #1b1b1d;
    --card-edge: #262628;
    --blue: #1f8fe3;
    --blue-deep: #1565c8;
    --ghost: #2e2e31;
    --text: #f2f2f2;
    --rule: #e6e6e6;
  }
  * { margin: 0; padding: 0; box-sizing: border-box; }
  html, body {
    width: 1200px; height: 1189px; overflow: hidden;
    background: var(--stage);
  }
  .canvas { position: relative; width: 1200px; height: 1189px; }
  .card {
    position: absolute; left: 150px; width: 900px; height: 514px;
    background: var(--card);
    border: 1px solid var(--card-edge);
    border-radius: 34px;
    overflow: hidden;
  }
  .card--front { top: 50px; }
  .card--back { top: 624px; }

  .ghost-mark {
    position: absolute; left: 70px; top: 110px;
    width: 330px; height: 330px; border-radius: 50%;
    background: var(--ghost);
  }

  .wordmark {
    position: absolute;
    font-family: "Cinzel", serif; font-weight: 700;
    color: var(--blue);
    text-align: center;
  }
  .wordmark__name { display: block; font-size: 46px; letter-spacing: 1px; line-height: 1; }
  .wordmark__sub {
    display: flex; align-items: center; gap: 14px;
    font-size: 20px; letter-spacing: 9px; margin-top: 6px; line-height: 1;
  }
  .wordmark__sub::before, .wordmark__sub::after {
    content: ""; flex: 1; height: 2px; background: var(--rule);
  }
  .card--front .wordmark { left: 390px; top: 190px; width: 430px; }
  .card--front .mark-dot {
    position: absolute; left: 540px; top: 90px;
    width: 92px; height: 92px; border-radius: 50%;
    background: linear-gradient(135deg, var(--blue), var(--blue-deep));
  }

  .card--back .wordmark { left: 80px; top: 110px; width: 430px; }
  .card--back .mark-ring {
    position: absolute; left: 570px; top: 120px;
    width: 260px; height: 260px; border-radius: 50%;
    background: linear-gradient(135deg, var(--blue), var(--blue-deep));
  }

  .address {
    position: absolute; left: 84px; top: 265px;
    font-family: "Questrial", sans-serif; font-size: 21px;
    color: var(--text); line-height: 1.3;
  }
  .contacts {
    position: absolute; left: 84px; top: 345px; list-style: none;
    font-family: "Questrial", sans-serif; font-size: 21px; color: var(--text);
  }
  .contacts li { display: flex; align-items: center; gap: 12px; height: 34px; }
  .contacts svg { width: 24px; height: 24px; flex: none; }
</style>
</head>
<body>
<div class="canvas">

  <section class="card card--front">
    <div class="ghost-mark" role="img" aria-label="Faint enlarged brand mark area"></div>
    <div class="mark-dot"></div>
    <div class="wordmark">
      <span class="wordmark__name">MARCUS ELLERY</span>
      <span class="wordmark__sub">COACHING</span>
    </div>
  </section>

  <section class="card card--back">
    <div class="wordmark">
      <span class="wordmark__name">MARCUS ELLERY</span>
      <span class="wordmark__sub">COACHING</span>
    </div>
    <p class="address">1480 W. Harbor Ln.<br>Suite 4, Los Angeles 900,USA</p>
    <ul class="contacts">
      <li>
        <svg viewBox="0 0 24 24"><circle cx="12" cy="12" r="11" fill="none" stroke="#1f8fe3" stroke-width="1.5"/><path d="M8 7.5c1-.8 1.8-.5 2.2.4l.6 1.4c.2.6-.1 1-.6 1.3.5 1.2 1.3 2 2.5 2.5.3-.5.7-.8 1.3-.6l1.4.6c.9.4 1.2 1.2.4 2.2-2.8 2.6-9.4-4-7.8-7.8z" fill="#1f8fe3"/></svg>
        555-013-4826
      </li>
      <li>
        <svg viewBox="0 0 24 24"><circle cx="12" cy="12" r="11" fill="none" stroke="#1f8fe3" stroke-width="1.5"/><rect x="6.5" y="8" width="11" height="8" fill="none" stroke="#1f8fe3" stroke-width="1.4"/><path d="M6.5 8l5.5 4.5L17.5 8" fill="none" stroke="#1f8fe3" stroke-width="1.4"/></svg>
        hello@ellerycoach.com
      </li>
      <li>
        <svg viewBox="0 0 24 24"><circle cx="12" cy="12" r="11" fill="none" stroke="#1f8fe3" stroke-width="1.5"/><circle cx="12" cy="12" r="6" fill="none" stroke="#1f8fe3" stroke-width="1.3"/><ellipse cx="12" cy="12" rx="2.6" ry="6" fill="none" stroke="#1f8fe3" stroke-width="1.2"/><path d="M6 12h12" stroke="#1f8fe3" stroke-width="1.2"/></svg>
        www.ellerycoach.com
      </li>
    </ul>
    <div class="mark-ring"></div>
  </section>

</div>
</body>
</html>
```